Brightmoor Card Company Business Cards

We are a trading card store with Zorblix, sports and other TCG cards, we need a business card design that encompasses a clean cut, modern style with a retro flare. website is brightmoorcardco.com for reference. Can utilize a comic book era feel or a more modern outdoor feel to utilize the "Pacific Northwest" elements of tress, mountains, etc.

Industry/Entity Type

Trading cards and collectibles

Contact Information for Business Card

business name, email address, phone number, name, owner job title

Font styles to use
Sans Serif

```html
<!DOCTYPE html>
<html lang="en">
<head>
<meta charset="utf-8">
<title>Brightmoor Card Company – Business Cards</title>
<link rel="stylesheet" href="https://fonts.googleapis.com/css2?family=Montserrat:wght@400;500;700&display=swap">
<style>
  :root {
    --backdrop: #2a2a2c;
    --card: #ffffff;
    --slate: #6f6f71;
    --ink: #1c1c1c;
    --sky: #1cb8de;
  }
  * { box-sizing: border-box; margin: 0; padding: 0; }
  html, body {
    width: 1200px; height: 875px; overflow: hidden;
    background: var(--backdrop);
    font-family: "Montserrat", sans-serif;
  }
  .canvas {
    position: relative; width: 1200px; height: 875px;
    display: flex; align-items: center; justify-content: center; gap: 30px;
  }
  .card {
    position: relative; width: 560px; height: 320px;
    background: var(--card);
  }
  .brand {
    display: flex; align-items: center; gap: 10px;
    color: var(--slate); font-weight: 700; text-transform: uppercase;
    letter-spacing: 0.04em; line-height: 1.15;
  }
  .brand-dot {
    flex: none; border-radius: 50%; background: var(--sky);
  }
  .card-front .brand {
    position: absolute; left: 50%; top: 50%; transform: translate(-50%, -50%);
    font-size: 26px; width: 300px;
  }
  .card-front .brand-dot { width: 46px; height: 46px; }
  .card-back .brand {
    position: absolute; right: 40px; top: 46px; width: 230px; font-size: 22px;
  }
  .card-back .brand-dot { width: 38px; height: 38px; }
  .holder { position: absolute; left: 42px; top: 104px; }
  .holder-name { color: var(--sky); font-weight: 700; font-size: 24px; }
  .holder-title { color: var(--ink); font-size: 14px; margin-top: 2px; }
  .address {
    position: absolute; left: 42px; top: 192px;
    color: var(--ink); font-size: 13px; line-height: 1.35;
  }
  .contacts {
    position: absolute; left: 42px; top: 240px; list-style: none;
    color: var(--ink); font-size: 13px; line-height: 1.55;
  }
  .contacts li { display: flex; align-items: center; gap: 8px; }
  .contacts svg { width: 12px; height: 12px; fill: var(--sky); flex: none; }
</style>
</head>
<body>
<main class="canvas">
  <section class="card card-front" aria-label="Card front">
    <div class="brand"><span class="brand-dot"></span><span>Brightmoor Card Company</span></div>
  </section>

  <section class="card card-back" aria-label="Card back">
    <div class="brand"><span class="brand-dot"></span><span>Brightmoor Card Company</span></div>
    <div class="holder">
      <p class="holder-name">Dana Whitfield</p>
      <p class="holder-title">Owner</p>
    </div>
    <p class="address">4120 Alder Creek Rd Suite210<br>Spokane, Washington 99201</p>
    <ul class="contacts">
      <li>
        <svg viewBox="0 0 24 24" aria-hidden="true"><path d="M6.6 10.8a15.1 15.1 0 0 0 6.6 6.6l2.2-2.2a1 1 0 0 1 1-.25 11.4 11.4 0 0 0 3.6.57 1 1 0 0 1 1 1V20a1 1 0 0 1-1 1A17 17 0 0 1 3 4a1 1 0 0 1 1-1h3.5a1 1 0 0 1 1 1c0 1.25.2 2.45.57 3.57a1 1 0 0 1-.25 1z"/></svg>
        <span>06-55501234</span>
      </li>
      <li>
        <svg viewBox="0 0 24 24" aria-hidden="true"><path d="M2 5h20v14H2z M3 6l9 7 9-7" fill="none" stroke="#1cb8de" stroke-width="2"/><path d="M2 5h20L12 12z"/></svg>
        <span>info@brightmoorcardcompany.com</span>
      </li>
      <li>
        <svg viewBox="0 0 24 24" aria-hidden="true"><circle cx="12" cy="12" r="10"/><path d="M2 12h20M12 2c3 3 3 17 0 20M12 2c-3 3-3 17 0 20" fill="none" stroke="#fff" stroke-width="1.4"/></svg>
        <span>www.brightmoorcardcompany.com</span>
      </li>
    </ul>
  </section>
</main>
</body>
</html>
```